create a webpage for optometry practice

I'm looking to create a professional and elegant webpage for my practice. I prefer neutral earthy colors, but I am open to other ideas. I have included an image of my logo to be used in the process. This will be a page that will illustrate information about my practice and the kind of services we offer. I am in process of having the practice remodeled. So I don't have any photos of my practice to include yet.

Target Market(s)

My practice serves young and mature families.

Font styles to use
Sans Serif

Colors
33a6d7
86cfc6
85cae6
cadf82
3276b5
faa54b
abd036
f78c1e

Requirements
Must have
• I would need to incorporate information about my practice, services, insurance accepted, make appointment, contact us, and about our family.
Nice to have
• I would like to see something fresh, modern, and unique

```html
<!DOCTYPE html>
<html lang="en">
<head>
<meta charset="utf-8">
<title>Lumera Eye Care</title>
<link href="https://fonts.googleapis.com/css2?family=Open+Sans:ital,wght@0,300;0,400;0,600;0,700;1,400&display=swap" rel="stylesheet">
<style>
:root{
  --blue:#0a6ca8;
  --blue-dark:#075687;
  --blue-deep:#064b77;
  --green:#8dc63f;
  --lime:#b5d43a;
  --orange:#f7941e;
  --ink:#444;
  --muted:#777;
  --white:#fff;
}
*{margin:0;padding:0;box-sizing:border-box}
html,body{width:1200px;height:2323px;overflow:hidden}
body{font-family:"Open Sans",Arial,sans-serif;color:var(--ink);background:var(--white);position:relative}
.abs{position:absolute}
a{color:inherit;text-decoration:none}

/* header */
.site-header{left:0;top:0;width:1200px;height:124px;background:var(--white)}
.brand{left:99px;top:46px;display:flex;align-items:center;gap:10px}
.brand-dot{width:30px;height:30px;border-radius:50%;background:var(--blue)}
.brand-name{font-size:32px;font-weight:400;color:var(--blue);letter-spacing:-.5px}
.contact-item{display:flex;align-items:center;gap:12px;font-size:14px;color:var(--blue);top:26px}
.contact-icon{width:34px;height:34px;border-radius:50%;background:#e4e4e4;display:flex;align-items:center;justify-content:center}
.btn-appoint{left:902px;top:23px;width:199px;height:36px;background:var(--green);color:var(--white);font-size:12px;font-weight:700;display:flex;align-items:center;justify-content:center;gap:10px;border-radius:2px}
.main-nav{top:84px;font-size:13px;color:#555}
.main-nav span{position:absolute;white-space:nowrap;transform:translateX(-50%)}

/* tagline */
.tagline{left:0;top:124px;width:1200px;height:59px;background:var(--blue);color:var(--white);font-size:23px;font-weight:700;display:flex;align-items:center;justify-content:center}
.tagline em{font-style:normal;color:var(--lime)}

/* hero */
.hero{left:0;top:183px;width:1200px;height:410px;background:linear-gradient(90deg,#c9d6df 0%,#e9e3df 30%,#dfe5ea 55%,#f1f3f5 100%)}
.hero-arrow{top:185px;width:40px;height:40px;border-radius:50%;background:rgba(255,255,255,.35)}
.hero-copy{left:681px;top:100px;width:420px}
.hero-title{font-size:47px;font-weight:700;color:var(--blue);line-height:1.1}
.hero-sub{font-size:38px;font-weight:300;color:var(--green);line-height:1.1;margin-top:4px}
.hero-text{font-size:14.5px;color:#555;line-height:1.7;margin-top:14px}
.btn-orange{background:var(--orange);color:var(--white);font-size:12px;font-weight:700;display:flex;align-items:center;justify-content:center;border-radius:2px}

/* welcome */
.welcome{left:0;top:593px;width:1200px;height:302px;background:var(--blue);color:var(--white);text-align:center}
.welcome h2{margin-top:48px;font-size:28px;font-weight:700}
.welcome .lead{font-size:16px;font-weight:300;margin-top:6px}
.welcome p.body{width:766px;margin:24px auto 0;font-size:11.5px;line-height:2}
.feature{width:260px;text-align:center;transform:translateX(-50%);top:840px}
.feature-ring{width:106px;height:106px;margin:0 auto;border-radius:50%;background:var(--blue);display:flex;align-items:center;justify-content:center}
.feature-disc{width:90px;height:90px;border-radius:50%;background:radial-gradient(circle at 40% 35%,#fff 0%,#eef1f4 60%,#d5dbe1 100%);display:flex;align-items:center;justify-content:center}
.feature h3{font-size:13.5px;font-weight:700;color:#444;margin-top:20px}
.feature p{font-size:11.5px;color:var(--muted);line-height:1.95;margin-top:8px}

/* services */
.section-title{left:0;width:1200px;text-align:center}
.section-title h2{font-size:28px;font-weight:700;color:#444}
.section-title p{font-size:16px;font-weight:300;color:#555;margin-top:4px}
.service{top:1212px;width:231px}
.service-photo{width:231px;height:164px}
.service h3{font-size:13.5px;font-weight:700;color:#444;margin-top:18px}
.service p{font-size:11.5px;color:var(--muted);line-height:1.95;margin-top:6px}

/* about */
.about-photo{left:99px;top:1517px;width:404px;height:465px;background:radial-gradient(ellipse at 50% 45%,#e7c2a3 0%,#f3e2d6 45%,#ffffff 78%)}
.about-copy{left:562px;top:1556px;width:494px}
.about-copy h2{font-size:28px;font-weight:700;color:var(--blue)}
.about-copy h4{font-size:13.5px;font-weight:700;color:#555;line-height:1.6;margin-top:12px}
.about-copy p{font-size:11.5px;color:var(--muted);line-height:1.95;margin-top:10px}
.about-copy p + p{margin-top:22px}

/* footer */
.site-footer{left:0;top:1982px;width:1200px;height:291px;background:var(--blue);color:var(--white)}
.footer-col{top:40px}
.footer-col h5{font-size:12.5px;font-weight:700;letter-spacing:.2px}
.footer-col ul{list-style:none;margin-top:16px}
.footer-col li{font-size:11.5px;line-height:22px}
.quote{font-size:11px;font-style:italic;line-height:2;width:260px;margin:18px 0 0 22px;position:relative}
.quote-mark{font-size:26px;font-weight:700;font-style:normal;position:absolute;line-height:1}
.slider-arrows{left:262px;top:0;font-size:12px;letter-spacing:6px}
.author{display:flex;align-items:center;gap:16px;margin:16px 0 0 16px}
.author-avatar{width:52px;height:52px;border-radius:50%;background:#d8dde2;border:3px solid var(--white)}
.author b{display:block;font-size:11.5px;font-weight:700}
.author span{font-size:12.5px}
.social li{display:flex;align-items:center;gap:8px;line-height:1;margin-bottom:14px;font-size:11.5px}
.social-dot{width:29px;height:29px;border-radius:50%;background:var(--white)}
.footer-bar{left:0;top:2273px;width:1200px;height:50px;background:var(--blue-deep);color:var(--white);font-size:11.5px;display:flex;align-items:center;justify-content:center}
</style>
</head>
<body>

<header class="site-header abs">
  <div class="brand abs">
    <span class="brand-dot"></span>
    <span class="brand-name">LUMERA EYE</span>
  </div>

  <div class="contact-item abs" style="left:558px">
    <span class="contact-icon">
      <svg width="16" height="16" viewBox="0 0 24 24"><path d="M6.6 10.8a15.1 15.1 0 0 0 6.6 6.6l2.2-2.2c.3-.3.7-.4 1-.2 1.1.4 2.3.6 3.6.6.6 0 1 .4 1 1V20c0 .6-.4 1-1 1A17 17 0 0 1 3 4c0-.6.4-1 1-1h3.5c.6 0 1 .4 1 1 0 1.3.2 2.5.6 3.6.1.3 0 .7-.2 1z" fill="#888"/></svg>
    </span>
    <span>( 2480 ) 417 390</span>
  </div>
  <div class="contact-item abs" style="left:720px">
    <span class="contact-icon">
      <svg width="16" height="16" viewBox="0 0 24 24"><rect x="3" y="6" width="18" height="12" rx="1" fill="none" stroke="#888" stroke-width="2"/><path d="M3 7l9 6 9-6" fill="none" stroke="#888" stroke-width="2"/></svg>
    </span>
    <span>info@lumeraeye.com</span>
  </div>
  <a class="btn-appoint abs" href="#appointment">MAKE AN APPOINTMENT
    <svg width="9" height="6" viewBox="0 0 9 6"><path d="M1 1l3.5 3.5L8 1" fill="none" stroke="#fff" stroke-width="1.5"/></svg>
  </a>

  <nav class="main-nav abs" style="left:0;width:1200px">
    <span style="left:371px">Home</span>
    <span style="left:485px">About Practise</span>
    <span style="left:604px">Services</span>
    <span style="left:711px">Insurance</span>
    <span style="left:831px">Appointment</span>
    <span style="left:954px">Our family</span>
    <span style="left:1068px">Contact us</span>
  </nav>
</header>

<div class="tagline abs">WELL-EQUIPPED WITH THE LATEST&nbsp;<em>TECHNOLOGIES</em>&nbsp;AND&nbsp;<em>SPECIALIZED SERVICES</em></div>

<section class="hero abs" role="img" aria-label="Photo of a patient looking into an eye examination instrument">
  <span class="hero-arrow abs" style="left:34px"></span>
  <span class="hero-arrow abs" style="left:1126px"></span>
  <div class="hero-copy abs">
    <div class="hero-title">LUMERA</div>
    <div class="hero-sub">WE ARE A EYE CARE</div>
    <p class="hero-text">Lorem Ipsum is simply dummy text of the printing and typesetting industry has been the industry's...</p>
    <a class="btn-orange" href="#about" style="width:183px;height:52px;margin-top:24px">READ MORE INFO</a>
  </div>
</section>

<section class="welcome abs">
  <h2>WELCOME TO LUMERA EYE</h2>
  <p class="lead">LOREM IPSUM IS SIMPLY DUMMY TEXT OF THE PRINTING AND TYPESETTING INDUSTRY.</p>
  <p class="body">Lorem Ipsum is simply dummy text of the printing and typesetting industry. Lorem Ipsum has been the industry's standard dummy text ever since the 1500s, when an unknown printer took a galley of type and scrambled it to make a type specimen book. It has survived not only five centuries, but also the leap into electronic typesetting, remaining essentially unchanged. It was popularised in the 1960s...</p>
</section>

<div class="feature abs" style="left:294px">
  <div class="feature-ring"><div class="feature-disc">
    <svg width="46" height="34" viewBox="0 0 46 34"><ellipse cx="23" cy="17" rx="19" ry="9" fill="none" stroke="#f7941e" stroke-width="4"/></svg>
  </div></div>
  <h3>INSURANCE</h3>
  <p>Lorem Ipsum is simply dummy text of the printing and typesetting industry. Lorem Ipsum has been the industry's...</p>
</div>
<div class="feature abs" style="left:599px">
  <div class="feature-ring"><div class="feature-disc">
    <svg width="44" height="44" viewBox="0 0 44 44"><circle cx="19" cy="19" r="12" fill="none" stroke="#33a6d7" stroke-width="4"/><path d="M28 28l10 10" stroke="#33a6d7" stroke-width="5" stroke-linecap="round"/></svg>
  </div></div>
  <h3>APPOINTMENT</h3>
  <p>Lorem Ipsum is simply dummy text of the printing and typesetting industry. Lorem Ipsum has been the industry's...</p>
</div>
<div class="feature abs" style="left:903px">
  <div class="feature-ring"><div class="feature-disc">
    <svg width="44" height="44" viewBox="0 0 44 44"><circle cx="16" cy="20" r="8" fill="#33a6d7"/><circle cx="30" cy="16" r="8" fill="#85cae6"/><rect x="8" y="28" width="28" height="8" rx="4" fill="#3276b5"/></svg>
  </div></div>
  <h3>OUR FAMILY</h3>
  <p>Lorem Ipsum is simply dummy text of the printing and typesetting industry. Lorem Ipsum has been the industry's...</p>
</div>

<div class="section-title abs" style="top:1108px">
  <h2>OUR SERVICES</h2>
  <p>LOREM IPSUM IS SIMPLY DUMMY TEXT OF THE PRINTING AND TYPESETTING INDUSTRY.</p>
</div>

<div class="service abs" style="left:99px">
  <div class="service-photo" role="img" aria-label="Photo illustrating a laser eye scan" style="background:linear-gradient(90deg,#c7ddf5,#f0e4dc)"></div>
  <h3>LOREM IPSUM IS A DUMMY</h3>
  <p>Simply dummy text of the printing and typesetting industry.</p>
</div>
<div class="service abs" style="left:356px">
  <div class="service-photo" role="img" aria-label="Photo of an eye examination with a slit lamp" style="background:linear-gradient(90deg,#d9d9d9,#eae1d8)"></div>
  <h3>LOREM IPSUM IS A DUMMY</h3>
  <p>Simply dummy text of the printing and typesetting industry.</p>
</div>
<div class="service abs" style="left:613px">
  <div class="service-photo" role="img" aria-label="Close-up photo of a contact lens on a fingertip" style="background:radial-gradient(circle at 55% 45%,#5f8c8e,#b98d7a 55%,#d6b7a4)"></div>
  <h3>LOREM IPSUM IS A DUMMY</h3>
  <p>Simply dummy text of the printing and typesetting industry.</p>
</div>
<div class="service abs" style="left:870px">
  <div class="service-photo" role="img" aria-label="Photo of eye drops being applied" style="background:linear-gradient(135deg,#e9c9b6,#f5eae3)"></div>
  <h3>LOREM IPSUM IS A DUMMY</h3>
  <p>Simply dummy text of the printing and typesetting industry.</p>
</div>

<div class="about-photo abs" role="img" aria-label="Photo of a woman framing her eyes with her hands"></div>
<div class="about-copy abs" id="about">
  <h2>ABOUT LUMERA EYE</h2>
  <h4>LOREM IPSUM IS SIMPLY DUMMY TEXT OF THE PRINTING AND TYPESETTING INDUSTRY.</h4>
  <p>Lorem Ipsum is simply dummy text of the printing and typesetting industry. Lorem Ipsum has been the industry's standard dummy text ever since the 1500s, when an unknown printer took a galley of type and scrambled it to make a type specimen book. It has survived not only five centuries, but also the leap into electronic typesetting.</p>
  <p>Remaining essentially unchanged. It was popularised in the 1960s with the release of Letterfix sheets containing Lorem Ipsum passages, and more recently with desktop publishing software like Pagemill Press including versions of Lorem Ipsum.</p>
  <a class="btn-orange" href="#about" style="width:183px;height:53px;margin-top:26px">READ MORE INFO</a>
</div>

<footer class="site-footer abs">
  <div class="footer-col abs" style="left:115px;width:300px">
    <h5>TESTIMONIALS</h5>
    <span class="slider-arrows abs">‹ ›</span>
    <p class="quote"><span class="quote-mark" style="left:-22px;top:-2px">“</span>Simply dummy text of the printing and typesetting industry. Lorem Ipsum has been the industry's standard dummy text ever since the 1500s, when an unknown printer took a galley of type and scrambled it to make a type specimen book...<span class="quote-mark" style="right:-22px;bottom:-12px">”</span></p>
    <div class="author">
      <span class="author-avatar" role="img" aria-label="Portrait of the reviewer"></span>
      <div><b>MARCUS HOLDEN</b><span>Marketing Executive</span></div>
    </div>
  </div>
  <div class="footer-col abs" style="left:503px">
    <h5>WELCOME</h5>
    <ul><li>Home</li><li>About Practise</li><li>Services</li><li>Insurance</li><li>Appointment</li><li>Our family</li><li>Contact us</li></ul>
  </div>
  <div class="footer-col abs" style="left:715px">
    <h5>INFORMATION</h5>
    <ul><li>Privacy Policy</li><li>Terms &amp; Conditions</li><li>Sitemap</li></ul>
  </div>
  <div class="footer-col abs" style="left:941px">
    <h5>FOLLOW US</h5>
    <ul class="social">
      <li><span class="social-dot"></span>: Friendbook</li>
      <li><span class="social-dot"></span>: Chirper</li>
      <li><span class="social-dot"></span>: Linkup</li>
      <li><span class="social-dot"></span>: Circleplus</li>
    </ul>
  </div>
</footer>
<div class="footer-bar abs">© 2015. Lumera Eye. All rights reserved.</div>

</body>
</html>
```